Pelin Thai Massage Double Sided Flyer Luxury

I require a double sided flyer
we are a Thai Massage Spa
Would like gold, deep purple and bronze colours
Something eye catching and looks professional

```html
<!DOCTYPE html>
<html lang="en">
<head>
<meta charset="utf-8">
<title>Pelin Thai Massage – Double Sided Flyer</title>
<link rel="stylesheet" href="https://fonts.googleapis.com/css2?family=Tinos:wght@400;700&family=Cormorant+Garamond:wght@400&family=Great+Vibes&display=swap">
<style>
  :root {
    --stage: #f8c650;
    --cocoa: #3b1a12;
    --cocoa-deep: #2e130c;
    --gold: #e9b22f;
    --cream: #fbf6f1;
    --pearl: #f1f0f2;
    --rose: #e0287a;
    --rose-soft: #f08bb0;
    --ink: #2a1a14;
    --taupe: #6f5a52;
  }
  * { box-sizing: border-box; margin: 0; padding: 0; }
  html, body {
    width: 1200px; height: 667px; overflow: hidden;
    background: var(--stage);
  }
  body { position: relative; font-family: "Tinos", "Times New Roman", serif; }

  .flyer {
    position: absolute; top: 89px;
    width: 345px; height: 489px; overflow: hidden;
    box-shadow: 0 10px 18px rgba(90, 50, 0, 0.18);
  }

  /* Front side */
  .flyer--front { left: 240px; background: var(--cocoa); }
  .brand {
    position: absolute; left: 0; width: 160px; top: 22px;
    display: flex; flex-direction: column; align-items: center;
  }
  .brand__dot {
    width: 34px; height: 34px; border-radius: 50%;
    background: var(--gold);
  }
  .brand__name {
    margin-top: 16px; color: var(--gold);
    font-size: 11.5px; font-weight: 400; letter-spacing: 0.2px;
  }
  .collage {
    position: absolute; left: 0; top: 107px; width: 345px; height: 274px;
    background: linear-gradient(120deg, #c79a5a 0%, #6e4a2c 30%, #d9c7b4 55%, #8a5a34 75%, #e9d9c7 100%);
  }
  .welcome {
    position: absolute; left: 54px; top: 123px;
    width: 242px; height: 242px; border-radius: 50%;
    background: #ffffff; overflow: hidden;
    box-shadow: 0 3px 10px rgba(0, 0, 0, 0.35);
    border: 4px solid #f4efec;
  }
  .welcome__photo {
    position: absolute; left: 0; top: 0; width: 100%; height: 60%;
    background: linear-gradient(180deg, #e8b9a0 0%, #f0cbb7 60%, #ffffff 100%);
  }
  .welcome__title {
    position: absolute; left: 0; right: 0; top: 150px; text-align: center;
    font-family: "Cormorant Garamond", "Times New Roman", serif;
    font-size: 27px; color: var(--taupe); line-height: 1;
  }
  .welcome__script {
    position: absolute; left: 20px; right: 0; top: 172px; text-align: center;
    font-family: "Great Vibes", cursive;
    font-size: 34px; color: var(--rose-soft); line-height: 1;
  }
  .intro {
    position: absolute; left: 30px; top: 408px; width: 288px;
    color: #f2e6de; font-size: 5.4px; line-height: 1.75;
  }
  .intro p + p { margin-top: 6px; }

  /* Back side */
  .flyer--back {
    left: 617px;
    background: linear-gradient(180deg, var(--pearl) 0%, #ffffff 45%, #ececee 100%);
  }
  .hero {
    position: absolute; left: 0; top: 0; width: 345px; height: 180px;
    background: linear-gradient(180deg, #e2c2ae 0%, #ecd6c8 55%, #f6eeea 82%, rgba(255,255,255,0) 100%);
  }
  .menu {
    position: absolute; left: 0; right: 0; top: 210px; text-align: center;
    color: var(--ink);
  }
  .menu__heading {
    color: var(--rose); font-size: 9px; letter-spacing: 3px;
    font-weight: 400; text-transform: uppercase;
  }
  .menu__lead { margin-top: 13px; font-size: 8.3px; line-height: 1.55; }
  .menu__treatment { margin-top: 13px; }
  .menu__treatment + .menu__treatment { margin-top: 15px; }
  .menu__prices { margin-top: 14px; font-size: 8.3px; line-height: 1.55; }
  .menu__prices b { font-weight: 700; }
  .contact {
    position: absolute; left: 0; right: 0; top: 412px; height: 50px;
  }
  .contact__brand {
    position: absolute; left: 48px; top: 0; width: 100px;
    display: flex; flex-direction: column; align-items: center;
  }
  .contact__dot {
    width: 24px; height: 24px; border-radius: 50%;
    background: var(--cocoa);
  }
  .contact__name { margin-top: 10px; font-size: 7.4px; color: var(--ink); white-space: nowrap; }
  .contact__rule {
    position: absolute; left: 149px; top: 2px; width: 1px; height: 44px;
    background: #cfc9c9;
  }
  .contact__details {
    position: absolute; left: 163px; top: 2px;
    font-size: 7.2px; line-height: 1.36; color: var(--ink);
    list-style: none;
  }
</style>
</head>
<body>

  <section class="flyer flyer--front">
    <header class="brand">
      <span class="brand__dot"></span>
      <span class="brand__name">Pelin Thai Massage</span>
    </header>

    <div class="collage" role="img" aria-label="Collage of spa photographs: oils, candles, towels, herbal compresses and flowers"></div>

    <div class="welcome">
      <div class="welcome__photo" role="img" aria-label="Photograph of a woman relaxing during a back massage"></div>
      <p class="welcome__title">Welcome to</p>
      <p class="welcome__script">Luxury</p>
    </div>

    <div class="intro">
      <p>Set in the heart of Elmcroft, Pelin Thai Massage will allow you to immerse yourself in a place where your wellbeing and rejuvenation is at the centre of wahat we do.</p>
      <p>Using Thai traditions, our highly trained therapists offer revitalising body treatments with their deep tissue massage techniques. In their hands, you will see and feel immediate results.</p>
    </div>
  </section>

  <section class="flyer flyer--back">
    <div class="hero" role="img" aria-label="Photograph of a woman receiving a shoulder massage on white towels with orchids"></div>

    <div class="menu">
      <h2 class="menu__heading">Massages</h2>
      <p class="menu__lead">Restore balance. Revive your senses. Discover all the ways Pelin<br>Thai Massage can breathe new life into your body and soul.</p>

      <div class="menu__treatment">
        <h3 class="menu__heading">Deep Tissue Massage</h3>
        <p class="menu__prices"><b>60 minutes £45</b> Oil massage personalised, light to firm pressure<br><b>90 minutes £55</b> Oil massage, medium to firm pressure</p>
      </div>

      <div class="menu__treatment">
        <h3 class="menu__heading">Thai Floor Tradtional Massage</h3>
        <p class="menu__prices"><b>60 minutes £45</b> Dry massage, medium to firm<br>pressure applying stretching technique</p>
      </div>
    </div>

    <footer class="contact">
      <div class="contact__brand">
        <span class="contact__dot"></span>
        <span class="contact__name">Pelin Thai Massage</span>
      </div>
      <span class="contact__rule"></span>
      <ul class="contact__details">
        <li>Pelin Thai Massage</li>
        <li>42 Willow Row, Harrowgate HG4 2QT</li>
        <li>0142 7780259</li>
        <li>www.pelinthaimassage.co.uk</li>
      </ul>
    </footer>
  </section>

</body>
</html>
```